Beauty & Wellness business needs a flyer to describe a multitude of therapy

I would like a flyer to represent my company. i would like it to have the form of a pamphlet 6 pages. The flyer should be in french if possible, but english also is okay. I'll upload a word file that illustrate what i would like, but it can be of course other images, this is just an example. And the text includes all the services we provide, some small description might be added if you think it's worth it from design point of view.
Target Market(s)
The market is seasonal. it's mostly winter for skiers, so wealthy and sporty people, and attentive to nature. But i also want to promote the brand for locals all year long, with reasonable pricing.
Industry/Entity Type
Wellness & aesthetics
Look and feel

```html
<!DOCTYPE html>
<html lang="fr">
<head>
<meta charset="utf-8">
<title>Alma Studio – Beauty &amp; Therapy</title>
<link href="https://fonts.googleapis.com/css2?family=Cinzel:wght@400;600;700&family=Playfair+Display:ital,wght@0,400;0,600;1,400&family=Arimo:wght@400&display=swap" rel="stylesheet">
<style>
  :root{
    --pink:#d93f96;
    --pink-soft:#e86aae;
    --yellow:#eeb214;
    --yellow-deep:#e3a40f;
    --plum:#6b1f55;
    --grey:#d4d3d8;
    --grey-light:#e9e7ec;
    --white:#ffffff;
    --ink:#3b3340;
    --bg:#f3f3f3;
  }
  *{box-sizing:border-box;margin:0;padding:0}
  html,body{width:1142px;height:1200px;overflow:hidden;background:var(--bg)}
  body{position:relative;font-family:"Playfair Display",serif;color:var(--ink)}

  .spread{position:absolute;left:188px;width:765px;height:540px;display:flex;box-shadow:0 6px 18px rgba(0,0,0,.12);overflow:hidden}
  .spread--outside{top:22px}
  .spread--inside{top:630px}
  .panel{position:relative;width:255px;height:540px;overflow:hidden;padding:18px 16px}

  .photo{display:block;width:100%}
  .frame{border:1px solid var(--pink-soft);padding:5px;background:transparent}

  /* outside: services panel */
  .panel--services{background:var(--grey-light)}
  .heading-caps{font-family:"Cinzel",serif;font-weight:600;font-size:13px;letter-spacing:.5px;color:var(--ink);line-height:1.2}
  .panel--services .heading-caps{text-align:right;margin-bottom:8px}
  .panel--services .heading-caps--second{margin-top:12px}
  .services-waxing{height:150px;background:linear-gradient(135deg,#5c4a43 0%,#b8968a 50%,#efe3dc 100%)}
  .services-brows{height:110px;background:linear-gradient(120deg,#e6d6cc,#c8a592 60%,#f4ece7)}
  .services-gallery{position:absolute;left:0;right:0;bottom:0;height:150px;background:linear-gradient(100deg,#8c7a70,#d7bfae 45%,#a48b7c 80%,#6f6a68)}

  /* outside: contact panel */
  .panel--contact{background:var(--yellow);display:flex;flex-direction:column;align-items:center;padding-top:150px}
  .brand{display:flex;align-items:center;gap:8px;font-family:"Cinzel",serif;font-weight:700;color:var(--plum);letter-spacing:2px}
  .brand__dot{width:14px;height:14px;border:2px solid var(--plum);border-radius:50%}
  .panel--contact .brand{font-size:18px;margin-bottom:22px}
  .contact-line{width:180px;text-align:center;font-family:"Arimo",sans-serif;font-size:9.5px;letter-spacing:1.2px;color:var(--white);padding:5px 0;border-bottom:1px solid rgba(107,31,85,.35)}
  .contact-phone{font-size:13px;letter-spacing:2px;border-bottom:0}
  .contact-bar{width:150px;height:4px;background:#8d8a8e;margin:6px 0 8px}
  .contact-address{font-family:"Arimo",sans-serif;font-size:9.5px;color:#1e1a1c}

  /* outside: cover */
  .panel--cover{background:var(--grey);padding:34px 20px 0;text-align:center}
  .panel--cover .brand{justify-content:center;font-size:21px}
  .cover-tagline{font-family:"Playfair Display",serif;font-style:italic;font-size:17px;color:#5a5560;margin-top:6px;padding-bottom:3px;border-bottom:1px solid #8d8a8e}
  .cover-web{font-size:9px;letter-spacing:1px;color:#5a5560;margin-top:4px}
  .cover-photo{position:absolute;left:0;right:0;top:160px;bottom:0;background:linear-gradient(160deg,#ece6df 0%,#c9855a 35%,#b9a08c 60%,#5f6a3e 100%)}

  .wave{position:absolute;left:0;bottom:0;width:100%}

  /* inside: face panel */
  .panel--face{background:var(--white)}
  .title-script{font-family:"Playfair Display",serif;font-size:15px;color:var(--pink);text-align:right;margin-bottom:8px}
  .face-mask{height:95px;background:linear-gradient(120deg,#e9e3de,#cdb7aa 55%,#f6f2ef)}
  .face-light{height:85px;background:linear-gradient(120deg,#3a0a08,#c2281a 50%,#5a1610)}
  .face-needling{height:80px;background:linear-gradient(120deg,#e7cfc0,#b89280 55%,#3a5aa8)}
  .service-list{list-style:none;margin:6px 0;font-size:10.5px;line-height:1.3;text-align:center}
  .service-list li{padding:1.5px 0;border-bottom:1px solid var(--yellow)}

  /* inside: massage panel */
  .panel--massage{background:var(--pink);color:var(--white)}
  .panel--massage .heading-caps{color:var(--white);font-size:14px;margin-bottom:10px}
  .massage-grid{display:flex;gap:8px}
  .bullet-list{list-style:none;font-size:10.5px;flex:1}
  .bullet-list li{display:flex;align-items:center;gap:6px;padding:1.5px 0}
  .bullet-list li::before{content:"";flex:none;width:7px;height:7px;border-radius:50%;background:radial-gradient(circle at 35% 35%,#fff,#a9a9ae)}
  .massage-thumbs{width:82px;display:flex;flex-direction:column;gap:4px}
  .thumb{height:44px;border:2px solid var(--white)}
  .thumb--stones{background:linear-gradient(120deg,#f2eae4,#4a3b34)}
  .thumb--back{background:linear-gradient(120deg,#e2cbbd,#9b7a6a)}
  .thumb--legs{background:linear-gradient(120deg,#d5d0cd,#7c7570)}
  .thumb--herbal{background:linear-gradient(120deg,#5a4639,#c7ab8c)}
  .massage-pair{display:flex;gap:4px;margin-top:10px}
  .massage-pair .photo{height:66px;border:2px solid var(--white)}
  .massage-pair .photo:first-child{background:linear-gradient(120deg,#3e312c,#b48a76)}
  .massage-pair .photo:last-child{background:linear-gradient(120deg,#f3e9de,#d8b493)}
  .panel--massage .heading-caps.meso{text-align:center;margin:14px 0 8px}
  .meso-photo{height:110px;border:6px solid var(--white);background:linear-gradient(90deg,#f3efec,#c48b6a 45%,#b57a5a 60%,#f3efec)}

  /* inside: hands & feet panel */
  .panel--care{background:var(--grey)}
  .panel--care .heading-caps{color:var(--pink);text-align:center;font-size:13px}
  .care-list{list-style:none;font-size:10.5px;text-align:center;margin:6px 24px 10px}
  .care-list li{padding:2px 0;border-bottom:1px solid var(--yellow)}
  .care-hands{height:110px;background:linear-gradient(120deg,#f4efe9,#e3cbb8 55%,#f8f4f0)}
  .care-spa{height:110px;background:linear-gradient(120deg,#cfc9c4,#8f8883 50%,#ede8e4)}
  .panel--care .heading-caps.spa{margin-top:22px}
</style>
</head>
<body>

<section class="spread spread--outside">
  <div class="panel panel--services">
    <h2 class="heading-caps">Épilation masculine<br>et féminin</h2>
    <div class="frame"><div class="photo services-waxing" role="img" aria-label="Photos d'épilation à la cire sur le dos et les jambes"></div></div>
    <h2 class="heading-caps heading-caps--second">Design des sourcils</h2>
    <div class="frame"><div class="photo services-brows" role="img" aria-label="Soin et mise en forme des sourcils"></div></div>
    <div class="services-gallery" role="img" aria-label="Galerie de soins : maquillage, massage aux pochons"></div>
    <svg class="wave" viewBox="0 0 255 150" height="150" preserveAspectRatio="none" aria-hidden="true">
      <path d="M0 0 C90 10 150 40 255 20 L255 0 Z" fill="var(--grey-light)"/>
      <path d="M180 150 C215 120 235 110 255 105 L255 150 Z" fill="var(--pink)"/>
    </svg>
  </div>

  <div class="panel panel--contact">
    <div class="brand"><span class="brand__dot"></span>Alma Studio</div>
    <p class="contact-line">www.alma-studio.ch</p>
    <p class="contact-line">contact@alma-studio.ch</p>
    <p class="contact-line contact-phone">+41-790001122</p>
    <div class="contact-bar"></div>
    <p class="contact-address">Chemin des Prés 12, Valmont, Suisse</p>
    <svg class="wave" viewBox="0 0 255 90" height="90" preserveAspectRatio="none" aria-hidden="true">
      <path d="M0 30 C90 55 170 80 255 70 L255 90 L0 90 Z" fill="var(--pink)"/>
      <path d="M0 0 C40 20 60 30 0 40 Z" fill="var(--yellow-deep)"/>
    </svg>
  </div>

  <div class="panel panel--cover">
    <div class="brand"><span class="brand__dot"></span>Alma Studio</div>
    <p class="cover-tagline">Beauty &amp; Therapy</p>
    <p class="cover-web">www.alma-studio.ch</p>
    <div class="cover-photo" role="img" aria-label="Portrait d'une cliente aux cheveux bouclés appliquant une crème"></div>
    <svg class="wave" viewBox="0 0 255 80" height="80" preserveAspectRatio="none" aria-hidden="true">
      <path d="M0 10 C80 30 170 20 255 0 L255 80 L0 80 Z" fill="var(--yellow)"/>
      <path d="M0 55 C90 75 170 70 255 60 L255 80 L0 80 Z" fill="var(--pink)"/>
    </svg>
  </div>
</section>

<section class="spread spread--inside">
  <div class="panel panel--face">
    <h2 class="title-script">Nos traitements du visage</h2>
    <div class="frame"><div class="photo face-mask" role="img" aria-label="Application d'un masque pour le visage"></div></div>
    <ul class="service-list">
      <li>Soin du visage classique</li>
      <li>Fils de collagènes</li>
      <li>Thérapie au plâtre</li>
      <li>Plasma Lift</li>
    </ul>
    <div class="frame"><div class="photo face-light" role="img" aria-label="Séance de luminothérapie rouge"></div></div>
    <ul class="service-list">
      <li>Chromothérapie</li>
      <li>Aromathérapie</li>
      <li>Needling</li>
    </ul>
    <div class="frame"><div class="photo face-needling" role="img" aria-label="Soin de microneedling"></div></div>
  </div>

  <div class="panel panel--massage">
    <h2 class="heading-caps">Nos massages maisons</h2>
    <div class="massage-grid">
      <ul class="bullet-list">
        <li>Sportif</li>
        <li>Pierre chaude</li>
        <li>Aryuvédique Pindas</li>
        <li>Guasha</li>
        <li>Bambou</li>
        <li>Drainage lymphatique</li>
        <li>Pour femmes enceintes</li>
        <li>Réflexologie</li>
        <li>Relaxant</li>
        <li>Shiatsu</li>
        <li>Deep tissue</li>
      </ul>
      <div class="massage-thumbs">
        <div class="thumb thumb--stones" role="img" aria-label="Massage aux pierres chaudes"></div>
        <div class="thumb thumb--back" role="img" aria-label="Massage du dos"></div>
        <div class="thumb thumb--legs" role="img" aria-label="Drainage des jambes"></div>
        <div class="thumb thumb--herbal" role="img" aria-label="Pochons aux herbes"></div>
      </div>
    </div>
    <div class="massage-pair">
      <div class="photo" role="img" aria-label="Massage sportif"></div>
      <div class="photo" role="img" aria-label="Massage relaxant aux pochons"></div>
    </div>
    <h2 class="heading-caps meso">Méso Cellulite</h2>
    <div class="photo meso-photo" role="img" aria-label="Traitement anti-cellulite"></div>
  </div>

  <div class="panel panel--care">
    <h2 class="heading-caps">Manicure &amp; Pédicure</h2>
    <ul class="care-list">
      <li>Semi permanent</li>
      <li>Fibre de verre</li>
      <li>Gel</li>
    </ul>
    <div class="frame"><div class="photo care-hands" role="img" aria-label="Soin des mains et des pieds"></div></div>
    <h2 class="heading-caps spa">Spa des pieds</h2>
    <ul class="care-list">
      <li>Argile thérapie</li>
      <li>Paraffine</li>
      <li>Plasma</li>
    </ul>
    <div class="frame"><div class="photo care-spa" role="img" aria-label="Fauteuils de spa des pieds"></div></div>
  </div>
</section>

</body>
</html>
```